BASTION.
Resolve, Survive & Rebuild
Additional info for a "Subtagline"-"" A comprehensive collection of survival techniques, tricks, tools and tactics."" We are creating a book that will be used as a field manual during and after a catastrophic event, i.e. Hurricane, Earthquake, Civil Unrest, Government overturn, Pelage.. etc.. This manual will be a how to guides on how to survive using items found in an urban environment i.e. how to make a battery using household chemicals, how to brew your own alcohol using everyday items found in a junkyard, how to build your own hydroponic garden using old gutters from a abandoned home.
Business Opportunities
2012 end of world believers, Outdoorsmen, Off the grid life styles.. We are also trying to target people who just want to be prepared for any type of life changing global catastraphy. Wether people admit it or not most think in the back of their mind that something will happen some day. Most people have once or twice looked on line for guides on how to survive after shit hits the fan.. We are trying to target individuals that like the tv shows "the orchard" "dust to dawn" "Ember Crossing"
We would like the book cover to be very simple. The book should have a somewhat sleek refined upscale look and should be designed with not just the "crazies" in mind. The books is meant to be a resource so super fancy photos all over might not provide any value... If you were stuck with only this book to help you figure out where to find food, how to lead people, how to rebuild a tribe/civilization you would want every space filled with information that will help you survive. We also would like to make sure it is easy to find so we do not want it to blend in with "surroundings" if someone left the book in a pile of leaves and the book cover had a camo look to it, it might get lost. That would be bad. This book will also be printed on waterproof and fire resistant paper... it will last for years and in the event of a global changing event this book could get pased on from generation to generation.

```html
<!DOCTYPE html>
<html lang="en">
<head>
<meta charset="utf-8">
<title>BASTION. — Resolve, Survive &amp; Rebuild</title>
<link rel="stylesheet" href="https://fonts.googleapis.com/css2?family=Anton&family=Black+Ops+One&family=Open+Sans:wght@700&display=swap">
<style>
  :root {
    --page: #ffffff;
    --frame: #0d0b0a;
    --cover-light: #fbb53c;
    --cover-mid: #f59a2c;
    --cover-edge: #e8762a;
    --ink: #17110d;
    --rust: #8a2a14;
    --signal-red: #d9322a;
    --glow: #f7e04a;
  }
  html, body {
    margin: 0;
    padding: 0;
    width: 1200px;
    height: 799px;
    overflow: hidden;
    background: var(--page);
  }
  .canvas {
    position: relative;
    width: 1200px;
    height: 799px;
  }
  .book-cover {
    position: absolute;
    left: 155px;
    top: 10px;
    width: 675px;
    height: 780px;
    background: var(--frame);
  }
  .cover-panel {
    position: absolute;
    left: 20px;
    top: 20px;
    right: 20px;
    bottom: 20px;
    background: radial-gradient(ellipse at 50% 45%, var(--cover-light) 0%, var(--cover-mid) 55%, var(--cover-edge) 100%);
    text-align: center;
  }
  .emblem-art {
    position: absolute;
    left: 90px;
    top: 30px;
    width: 455px;
    height: 100px;
    background: radial-gradient(ellipse 70px 45px at 50% 55%, rgba(247,224,74,0.9) 0%, rgba(160,200,60,0.5) 45%, rgba(245,154,44,0) 100%);
  }
  .title {
    position: absolute;
    left: 0;
    right: 0;
    top: 120px;
    margin: 0;
    font-family: "Anton", sans-serif;
    font-weight: 400;
    font-size: 150px;
    line-height: 1;
    letter-spacing: 4px;
    color: var(--ink);
  }
  .tagline {
    position: absolute;
    left: 0;
    right: 0;
    top: 290px;
    margin: 0;
    font-family: "Black Ops One", sans-serif;
    font-size: 27px;
    letter-spacing: 2px;
    color: var(--rust);
    text-transform: uppercase;
  }
  .atom-bulb-art {
    position: absolute;
    left: 130px;
    top: 345px;
    width: 375px;
    height: 300px;
    border-radius: 50%;
    background: radial-gradient(circle at 50% 30%, rgba(247,224,74,0.85) 0%, rgba(251,190,70,0.5) 30%, rgba(245,154,44,0) 70%);
  }
  .subtagline {
    position: absolute;
    left: 0;
    right: 0;
    top: 648px;
    margin: 0;
    font-family: "Open Sans", sans-serif;
    font-weight: 700;
    font-size: 15px;
    line-height: 22px;
    color: var(--signal-red);
  }
  .down-marker {
    position: absolute;
    left: 299px;
    top: 702px;
    width: 38px;
    height: 30px;
  }
</style>
</head>
<body>
  <main class="canvas">
    <section class="book-cover">
      <div class="cover-panel">
        <div class="emblem-art" role="img" aria-label="Glowing green pyramid emblem with a lightning streak"></div>
        <h1 class="title">BASTION.</h1>
        <p class="tagline">Resolve, Survive &amp; Rebuild</p>
        <div class="atom-bulb-art" role="img" aria-label="Line illustration of a light bulb circled by atomic orbits"></div>
        <p class="subtagline">A guide to post catastrophic event survival,<br>in a complex and modern urban environment.</p>
        <svg class="down-marker" viewBox="0 0 38 30" aria-hidden="true">
          <polygon points="0,0 38,0 19,30" fill="var(--signal-red)"/>
        </svg>
      </div>
    </section>
  </main>
</body>
</html>
```